Brightwell Pipeworks

We need a webpage designed for http://www.brightwellpipeworks.example/. Something clean, and focused.

Homepage needs some call to action at the top, also this is a local business so things like telephone, address, ratings, social media, should be present.

We like contact forms above the fold.

http://www.ravodinplumbing.example/ is a website that was referenced, although I personally think it looks "old". Something more modern.

http://www.tedsplumbing.example/ has the pieces we like, bit is not visually appealing.

http://mintwashcrewok.example/ is nice looking but doesnt have a good call to action

http://www.lanterly.example/ and http://www.theneighborpass.example/ is great

Target Market(s)

Adluts, homeowners

Industry/Entity Type

Business

Font styles to use
Sans Serif

Requirements
Must have
• Homepage needs some call to action form at the top, also this is a local business so things like telephone, address, ratings, social media,
Nice to have
• Prefer layouts that have a fixed max width - not that stretch off the screen
Should not have
• don't overdo "plumber theme" - we want professional, clean and uncluttered. No generic pictures of "plumbers" or cartoon plumbers.

```html
<!DOCTYPE html>
<html lang="en">
<head>
<meta charset="utf-8">
<title>Brightwell Pipeworks</title>
<link rel="stylesheet" href="https://fonts.googleapis.com/css2?family=Open+Sans:wght@300;400;600&display=swap">
<style>
:root{
  --blue:#2f6fcc;
  --ink:#4a4f57;
  --heading:#7f858b;
  --body:#989ea4;
  --panel:#5c5c5c;
  --field:#4b4b4b;
  --green:#7aab4a;
  --dot:#d3d6d9;
  --white:#fff;
}
*{margin:0;padding:0;box-sizing:border-box}
html,body{width:778px;height:1200px;overflow:hidden;background:var(--white)}
body{position:relative;font-family:"Open Sans",Arial,sans-serif;font-weight:400;color:var(--body)}
.abs{position:absolute}
.brand{font-size:14px;font-weight:600;color:var(--ink);display:flex;align-items:center;gap:6px;line-height:18px}
.brand-dot{width:12px;height:12px;border-radius:50%;background:var(--blue)}
.top-call{left:461px;top:6px;font-size:10px;color:var(--blue);font-weight:400;line-height:13px}
.top-call span{color:var(--heading);font-weight:300}
.social{display:flex;gap:6px}
.social i{display:block;width:13px;height:13px;border-radius:50%;background:var(--dot)}
.nav{left:425px;top:37px;display:flex;gap:19px;font-size:6.5px;color:var(--heading);text-transform:uppercase}
.hero{left:0;top:72px;width:778px;height:267px;background:linear-gradient(100deg,#c9ccd1 0%,#e6e8ec 35%,#d2c0b4 65%,#c79a85 100%)}
.caption{left:120px;top:163px;width:169px;height:96px;background:rgba(110,120,150,.6);color:var(--white);padding:14px 8px}
.caption h2{font-size:10px;font-weight:300;margin-bottom:6px}
.caption p{font-size:7px;line-height:10px;font-weight:400}
.arrow{top:196px;width:20px;height:20px;background:rgba(120,120,120,.7);display:flex;align-items:center;justify-content:center}
.dots{left:402px;top:328px;display:flex;gap:2px}
.dots i{display:block;width:50px;height:2px;background:rgba(255,255,255,.4)}
.dots i:first-child{background:var(--white)}
.contact{left:494px;top:90px;width:165px;height:232px;background:var(--panel);border-radius:3px;color:var(--white)}
.contact > *{position:absolute;left:14px;width:137px}
.contact h3{top:9px;font-size:9px;font-weight:400;text-align:center;line-height:12px}
.contact label{font-size:6px;font-weight:400;line-height:8px}
.contact .field{height:16px;background:var(--field);border-radius:2px}
.contact .msg{height:47px}
.contact .submit{top:201px;height:19px;background:var(--green);border-radius:2px;font-size:7px;font-weight:600;text-align:center;line-height:19px}
.intro{left:204px;top:366px;width:370px;text-align:center}
.intro h2,.services h2{font-size:10px;font-weight:300;color:var(--heading);margin-bottom:10px;line-height:13px}
.intro p{font-size:7.4px;line-height:10.3px;color:var(--body);margin-bottom:10px}
.services{left:0;top:644px;width:778px;text-align:center}
.cards{position:absolute;left:119px;top:35px;display:flex;gap:15px}
.card{width:170px}
.card .ph{height:96px}
.card h3{font-size:8.5px;font-weight:300;color:var(--heading);margin:11px 0 8px}
.card p{font-size:6.5px;line-height:10.3px;color:var(--body)}
.next{left:680px;top:716px}
.band{left:0;top:876px;width:778px;height:185px;background:var(--blue)}
.video{left:119px;top:895px;width:263px;height:147px;background:linear-gradient(180deg,#5a4a3a,#3a3028);color:var(--white)}
.video .title{position:absolute;left:7px;top:4px;font-size:5.5px;font-weight:400}
.video .bar{position:absolute;left:0;bottom:0;width:100%;height:12px;background:rgba(0,0,0,.7)}
.video .progress{position:absolute;left:0;bottom:12px;width:100%;height:2px;background:#777}
.video .progress i{display:block;width:24px;height:2px;background:#e52d27}
.band-text{left:395px;top:896px;width:262px;color:var(--white)}
.band-text h2{font-size:10px;font-weight:300;margin-bottom:8px;line-height:13px}
.band-text p{font-size:7.6px;line-height:10.3px;margin-bottom:10px;font-weight:400}
.foot-about{left:119px;top:1110px;width:122px;font-size:6.5px;line-height:10.2px;color:var(--body)}
.foot-call{left:285px;top:1076px;text-align:center}
.foot-call h4,.foot-social h4{font-size:8px;font-weight:300;color:var(--heading);margin-bottom:10px}
.foot-call p{font-size:10px;color:var(--heading)}
.foot-social{left:396px;top:1076px}
.foot-social .social i{width:16px;height:16px;margin-right:11px}
.badge-a{left:545px;top:1078px;width:66px;height:58px;border-radius:50% 50% 12px 12px;background:var(--blue)}
.badge-b{left:622px;top:1078px;width:37px;height:52px;border:2px solid var(--blue);background:#e9eef8}
.copyright{left:119px;top:1186px;font-size:6px;color:var(--body)}
</style>
</head>
<body>

<div class="abs top-call">Call: <span>555-014-2077</span></div>
<div class="abs social" style="left:573px;top:6px"><i></i><i></i><i></i><i></i><i></i></div>
<div class="abs brand" style="left:120px;top:32px"><span class="brand-dot"></span>Brightwell Pipeworks</div>
<nav class="abs nav"><span>Home</span><span>About Us</span><span>Services</span><span>Testimonials</span><span>Contact</span></nav>

<div class="abs hero" role="img" aria-label="Photo of a hand tightening a chrome pipe fitting with a red wrench"></div>
<div class="abs caption">
  <h2>Brightwell Pipeworks</h2>
  <p>Ut tortor turpis, elementum vitae urna vel, accumsan aliquet mi.Nullam viverra ali quam augue, vitae dapibus purus imperdi et quis.</p>
</div>
<div class="abs arrow" style="left:29px"><svg width="8" height="10" viewBox="0 0 8 10"><path d="M6 1 2 5l4 4" fill="none" stroke="#fff" stroke-width="1.6"/></svg></div>
<div class="abs arrow" style="left:728px"><svg width="8" height="10" viewBox="0 0 8 10"><path d="M2 1l4 4-4 4" fill="none" stroke="#fff" stroke-width="1.6"/></svg></div>
<div class="abs dots"><i></i><i></i><i></i></div>

<form class="abs contact">
  <h3>CONTACT US</h3>
  <label style="top:36px">Name:</label><div class="field" style="top:44px"></div>
  <label style="top:69px">Email:</label><div class="field" style="top:78px"></div>
  <label style="top:102px">Phone:</label><div class="field" style="top:111px"></div>
  <label style="top:135px">Message:</label><div class="field msg" style="top:144px"></div>
  <div class="submit">SUBMIT</div>
</form>

<section class="abs intro">
  <h2>Los Angeles Best Plumber</h2>
  <p>Plumbers with a Service Area from Burbank to Ontario, all of Orange County,<br>From Seal Beach to Laguna Beach, Anaheim and Corona, All Points In-Between</p>
  <p>-You approve the price before we start work.<br>-Same-day service generally available.<br>-Always FREE work estimates.<br>-Call today to find out how we can help!</p>
  <p>Brightwell Pipeworks is the Sole Authorized Dealer and Installer for Clearbrook Water Systems in Orange County, Riverside and San Bernardino Counties, and San Gabriel Valley, Southeast Los Angeles.</p>
  <p>Nam dictum id ante id accumsan. Aenean ac nunc a lorem porta cursus quis eget est. Quisque congue ipsum in sem placerat, ut semper odio mollis. Interdum et malesuada fames ac ante ipsum primis in faucibus.</p>
  <p>Maecenas orci sem, interdum in sagittis ut, faucibus ut quam. Pellentesque mattis, nisi at pulvinar rutrum, ante libero semper est, eget ultrices neque nisl a ligula.</p>
  <p>Ut tortor turpis, elementum vitae urna vel, accumsan aliquet mi.Nullam viverra aliquam augue, vitae dapibus purus imperdiet quis.</p>
</section>

<section class="abs services">
  <h2>Our Services</h2>
  <div class="cards">
    <div class="card">
      <div class="ph" role="img" aria-label="Diagram of trenchless sewer repair with before and after pipe views" style="background:linear-gradient(180deg,#e8e6e0 0%,#e8e6e0 55%,#b8743e 56%,#9a5a2a 100%)"></div>
      <h3>Trenchless Sewer Repair</h3>
      <p>Lorem ipsum dolor sit amet, consectetur adipiscing elit. Etiam quis tincidunt justo. Pellentesque venenatis auctor nisl, a placerat nunc mattis sed. Ut ac tellus fringilla, pretium justo in, rhoncus ipsum.</p>
    </div>
    <div class="card">
      <div class="ph" role="img" aria-label="Photo of a new black sewer pipe laid in broken clay soil" style="background:linear-gradient(160deg,#8a5f4e,#5a3a30 50%,#7d5545)"></div>
      <h3>Sewer Pipe Bursting Repair</h3>
      <p>Lorem ipsum dolor sit amet, consectetur adipiscing elit. Etiam quis tincidunt justo. Pellentesque venenatis auctor nisl, a placerat nunc mattis sed. Ut ac tellus fringilla, pretium justo in, rhoncus ipsum.</p>
    </div>
    <div class="card">
      <div class="ph" role="img" aria-label="Photo of a technician with a video inspection reel on a lawn" style="background:linear-gradient(180deg,#c8ccd0 0%,#b9bfb0 45%,#5e8a3a 60%,#4a7a2c 100%)"></div>
      <h3>Video Pipe Inspections</h3>
      <p>Lorem ipsum dolor sit amet, consectetur adipiscing elit. Etiam quis tincidunt justo. Pellentesque venenatis auctor nisl, a placerat nunc mattis sed. Ut ac tellus fringilla, pretium justo in, rhoncus ipsum.</p>
    </div>
  </div>
</section>
<svg class="abs next" width="12" height="20" viewBox="0 0 12 20"><path d="M2 2l8 8-8 8" fill="none" stroke="#d0d3d6" stroke-width="2"/></svg>

<section class="abs band"></section>
<div class="abs video" role="img" aria-label="Embedded video about water filtration systems, presenter in a kitchen">
  <div class="title">Safeguarding your water with the Clearbrook Water Systems Combo Series</div>
  <div class="progress"><i></i></div>
  <div class="bar">
    <svg class="abs" style="left:8px;top:3px" width="6" height="6" viewBox="0 0 6 6"><path d="M0 0l6 3-6 3z" fill="#fff"/></svg>
    <span class="abs" style="left:47px;top:3px;font-size:5px">0:29 / 6:15</span>
  </div>
</div>
<div class="abs band-text">
  <h2>Los Angeles Best Plumber</h2>
  <p>Brightwell Pipeworks is the Sole Authorized Dealer and Installer for Clearbrook Water Systems in Orange County, Riverside and San Bernardino Counties, and San Gabriel Valley, Southeast Los Angeles.</p>
  <p>Nam dictum id ante id accumsan. Aenean ac nunc a lorem porta cursus quis eget est. Quisque congue ipsum in sem placerat, ut semper odio mollis. Interdum et malesuada fames ac ante ipsum primis in faucibus.</p>
  <p>Maecenas orci sem, interdum in sagittis ut, faucibus ut quam. Pellentesque mattis, nisi at pulvinar rutrum, ante libero semper est, eget ultrices neque nisl a ligula.</p>
</div>

<div class="abs brand" style="left:119px;top:1082px"><span class="brand-dot"></span>Brightwell Pipeworks</div>
<p class="abs foot-about">Brightwell Pipeworks is the Sole Authorized Dealer and Installer for Clearbrook Water Systems in Orange County, Riverside and San Bernardino Counties, and San Gabriel Valley, Southeast Los Angeles.</p>
<div class="abs foot-call"><h4>Call Us</h4><p>555-014-2077</p></div>
<div class="abs foot-social"><h4>Stay Connected</h4><div class="social"><i></i><i></i><i></i><i></i><i></i></div></div>
<div class="abs badge-a" aria-label="Authorized dealer badge"></div>
<div class="abs badge-b" aria-label="Accreditation badge"></div>
<p class="abs copyright">©2006-2014 All content rights reserved by Brightwell Pipeworks &nbsp;|&nbsp; Check Our California Plumbing Contractor License Number 481207</p>

</body>
</html>
```